professional looking data specialist website

I've recently had a new logo designed and I'm now looking to get a professional looking website built. This is for a new company that specialises in data. We look to support companies with business intelligence, report modelling, data governance to new european legislation (GDPR). We are offer consultancy or we can attend site and complete work when required. Our target arket is united kingdom wide and we are specifically aiming at small to medium sized companies.

Target Market(s)

small to medium enterprise companies from all industries

Industry/Entity Type

Professional Service

Coding

Coded - Design and coding required

Number of Pages Required

4 page

Font styles to use
Sans Serif

Colors

Designer to choose colors to be used in the design.

Requirements
Must have
• Professional look including the company logo, need to have ability to request more information from us so needs a inquiries page, seperate pages for the different offerings, data governance, report modelling, business intelligence implementation, data protection
Nice to have
• any website interaction, animation, etc
Should not have
• too many colours, too busy pages, must look professional

```html
<!DOCTYPE html>
<html lang="en">
<head>
<meta charset="utf-8">
<title>Why Choose Us – Data Services</title>
<link href="https://fonts.googleapis.com/css2?family=Jost:wght@300;400;500&family=Josefin+Sans:wght@300;400&display=swap" rel="stylesheet">
<style>
  :root {
    --page-dark: #242f38;
    --panel-slate: #3e5566;
    --hero-grey: #62606f;
    --accent-blue: #8fc3d6;
    --text-light: #ffffff;
    --card-bg: #d9d9d9;
    --card-border: #e9e9e9;
    --card-text: #2a2a2a;
    --rule-dark: #141c22;
  }
  * { margin: 0; padding: 0; box-sizing: border-box; }
  html, body { width: 936px; height: 1200px; overflow: hidden; }
  body {
    position: relative;
    background: var(--page-dark);
    font-family: "Josefin Sans", sans-serif;
    color: var(--text-light);
  }
  .hero {
    position: absolute; left: 0; top: 0; width: 936px; height: 130px;
    background: linear-gradient(90deg, #5f5d6c 0%, #6b6977 50%, #5f5d6c 100%);
    border-bottom: 1px solid #7d8a96;
  }
  .hero-photo {
    position: absolute; left: 248px; top: 0; width: 440px; height: 130px;
    background: linear-gradient(90deg, #4d4c58 0%, #36363f 30%, #6e6e78 60%, #5c5c66 100%);
    opacity: .85;
  }
  .hero-button {
    position: absolute; left: 760px; top: 61px; width: 92px; height: 26px;
    border: 2px solid var(--text-light); border-radius: 13px;
    font-family: "Jost", sans-serif; font-weight: 500; font-size: 14px;
    line-height: 22px; text-align: center; color: var(--text-light);
  }
  .backdrop { position: absolute; left: 0; top: 0; }
  .section-heading { position: absolute; left: 0; width: 936px; text-align: center; }
  .section-heading h2 {
    font-family: "Jost", sans-serif; font-weight: 300; font-size: 38px;
    letter-spacing: 9px; line-height: 1;
  }
  .section-heading.news h2 { font-weight: 400; font-size: 40px; letter-spacing: 7px; }
  .section-heading p {
    font-family: "Jost", sans-serif; font-size: 17px; letter-spacing: 4px;
    color: var(--accent-blue); margin-top: 14px; line-height: 1;
  }
  .rule { position: absolute; height: 1px; background: var(--rule-dark); width: 183px; }
  .service { position: absolute; width: 320px; height: 100px; }
  .service svg { position: absolute; left: 0; top: 0; }
  .service h3 {
    position: absolute; left: 109px; top: 2px;
    font-family: "Josefin Sans", sans-serif; font-weight: 300; font-size: 16px;
    letter-spacing: .2px;
  }
  .service p {
    position: absolute; left: 109px; top: 24px; width: 230px;
    font-size: 12px; font-weight: 300; line-height: 15.5px;
  }
  .news-card {
    position: absolute; top: 787px; width: 252px; height: 374px;
    background: var(--card-bg); border: 1px solid var(--card-border);
    color: var(--card-text);
  }
  .news-image { width: 100%; height: 159px; position: relative; }
  .news-image.servers { background: linear-gradient(160deg, #33516a, #2c4558); }
  .news-image.tablet { background: linear-gradient(135deg, #d7e6ef 0%, #6b97bd 40%, #2a4560 100%); }
  .news-image.workshop { background: linear-gradient(90deg, #d0d3cc 0%, #b7b9ae 50%, #dcdcd6 100%); }
  .news-image svg { position: absolute; left: 106px; top: 60px; }
  .news-body { padding: 24px 21px 0 21px; }
  .news-date { font-size: 11px; font-weight: 400; letter-spacing: .2px; }
  .news-title {
    margin-top: 16px; font-size: 15.5px; font-weight: 300; line-height: 17px;
  }
  .news-excerpt { margin-top: 17px; font-size: 10px; font-weight: 300; line-height: 13.6px; width: 180px; }
  .news-link {
    position: absolute; left: 21px; top: 343px; font-size: 11px; font-weight: 300;
    display: flex; align-items: center; gap: 5px;
  }
</style>
</head>
<body>
  <header class="hero">
    <div class="hero-photo" role="img" aria-label="Photo of two business professionals in suits with arms crossed"></div>
    <div class="hero-button">Read More</div>
  </header>

  <svg class="backdrop" width="936" height="1200" aria-hidden="true">
    <polygon points="0,224 432,648 0,1144" fill="var(--panel-slate)"/>
  </svg>

  <section class="section-heading" style="top:198px">
    <h2>WHY CHOOSE US ?</h2>
    <p>OUR SERVICES</p>
  </section>
  <div class="rule" style="left:198px; top:254px"></div>
  <div class="rule" style="left:558px; top:254px"></div>

  <div class="service" style="left:85px; top:325px">
    <svg width="88" height="96" viewBox="-44 -48 88 96" fill="none" stroke="#fff" stroke-width="1.6">
      <path d="M-43,-17 L0,-48 L43,-17 M-43,17 L0,48 L43,17"/>
      <path d="M-2,-24 C-14,-28 -24,-20 -22,-10 C-28,-4 -26,8 -18,10 C-16,20 -6,22 -2,18 Z"/>
      <path d="M2,-24 C14,-28 24,-20 22,-10 C28,-4 26,8 18,10 C16,20 6,22 2,18 Z"/>
      <path d="M-14,-12 h6 v8 h-6 M-12,4 h8 M10,-14 v10 h6 M8,6 h8 M-8,-18 v6 M12,10 v-4"/>
    </svg>
    <h3>BUSINESS INTELLIGENCE</h3>
    <p>Lorem ipsum dolor sit amet, consectetur<br>Nam in ex in libero pellentesque<br>Proin lacus turpis</p>
  </div>

  <div class="service" style="left:544px; top:325px">
    <svg width="88" height="96" viewBox="-44 -48 88 96" fill="none" stroke="#fff" stroke-width="1.6">
      <path d="M-43,-17 L0,-48 L43,-17 M-43,17 L0,48 L43,17"/>
      <rect x="-20" y="-22" width="40" height="50" rx="4"/>
      <path d="M-8,-22 v-4 h16 v4 M-3,-26 a3,3 0 0 1 6,0"/>
    </svg>
    <h3>BUSINESS INTELLIGENCE</h3>
    <p>Lorem ipsum dolor sit amet, consectetur<br>Nam in ex in libero pellentesque<br>Proin lacus turpis</p>
  </div>

  <div class="service" style="left:85px; top:497px">
    <svg width="88" height="96" viewBox="-44 -48 88 96" fill="none" stroke="#fff" stroke-width="1.6">
      <path d="M-43,-17 L0,-48 L43,-17 M-43,17 L0,48 L43,17"/>
      <path d="M-12,-24 h22 l6,6 v8 M-6,-24 v-4 h22 l6,6 v10"/>
      <rect x="-22" y="-18" width="30" height="38" rx="3"/>
      <path d="M-16,-6 h12 M-16,2 h10 M-16,10 h10"/>
      <rect x="2" y="0" width="18" height="14" rx="2" fill="#fff"/>
      <path d="M5,0 v-5 a6,6 0 0 1 12,0 v5"/>
    </svg>
    <h3>BUSINESS INTELLIGENCE</h3>
    <p>Lorem ipsum dolor sit amet, consectetur<br>Nam in ex in libero pellentesque<br>Proin lacus turpis</p>
  </div>

  <div class="service" style="left:544px; top:497px">
    <svg width="88" height="96" viewBox="-44 -48 88 96" fill="none" stroke="#fff" stroke-width="1.6">
      <path d="M-43,-17 L0,-48 L43,-17 M-43,17 L0,48 L43,17"/>
      <circle cx="-6" cy="-12" r="8" fill="#fff" stroke="none"/>
      <path d="M-24,22 C-24,6 -16,2 -6,2 C4,2 12,6 12,22 Z" fill="#fff" stroke="none"/>
      <path d="M6,-24 h20 v14 h-12 l-5,5 v-5 h-3 Z"/>
      <path d="M10,-19 h12 M10,-15 h8"/>
    </svg>
    <h3>BUSINESS INTELLIGENCE</h3>
    <p>Lorem ipsum dolor sit amet, consectetur<br>Nam in ex in libero pellentesque<br>Proin lacus turpis</p>
  </div>

  <section class="section-heading news" style="top:660px">
    <h2>LATEST NEWS</h2>
    <p>UPDATES</p>
  </section>
  <div class="rule" style="left:198px; top:718px"></div>
  <div class="rule" style="left:558px; top:718px"></div>

  <article class="news-card" style="left:84px">
    <div class="news-image servers" role="img" aria-label="Photo of a server room with racks of equipment">
      <svg width="40" height="40" viewBox="0 0 40 40" fill="none" stroke="#fff" stroke-width="1.6">
        <circle cx="20" cy="20" r="19"/>
        <path d="M18,16 l3,-3 a3.5,3.5 0 0 1 5,5 l-3,3 M22,24 l-3,3 a3.5,3.5 0 0 1 -5,-5 l3,-3 M17,23 l6,-6"/>
      </svg>
    </div>
    <div class="news-body">
      <div class="news-date">JULY 15, 2017</div>
      <div class="news-title">LOREM IPSUM DOLOR SIT<br>AMET</div>
      <p class="news-excerpt">Lorem ipsum dolor sit amet, consectetur adipiscing elit. Curabitur arcu diam, ornare vitae blandit sed, mollis pulvinar tortor...</p>
    </div>
    <div class="news-link">Read More <svg width="6" height="9" viewBox="0 0 6 9"><path d="M1,1 L4.5,4.5 L1,8" fill="none" stroke="#222" stroke-width="1.6"/></svg></div>
  </article>

  <article class="news-card" style="left:342px">
    <div class="news-image tablet" role="img" aria-label="Photo of hands using a tablet and stylus over business charts"></div>
    <div class="news-body">
      <div class="news-date">JULY 15, 2017</div>
      <div class="news-title">LOREM IPSUM DOLOR SIT<br>AMET</div>
      <p class="news-excerpt">Lorem ipsum dolor sit amet, consectetur adipiscing elit. Curabitur arcu diam, ornare vitae blandit sed, mollis pulvinar tortor...</p>
    </div>
    <div class="news-link">Read More <svg width="6" height="9" viewBox="0 0 6 9"><path d="M1,1 L4.5,4.5 L1,8" fill="none" stroke="#222" stroke-width="1.6"/></svg></div>
  </article>

  <article class="news-card" style="left:600px">
    <div class="news-image workshop" role="img" aria-label="Photo of two technicians working with equipment in a data centre"></div>
    <div class="news-body">
      <div class="news-date">JULY 15, 2017</div>
      <div class="news-title">LOREM IPSUM DOLOR SIT<br>AMET</div>
      <p class="news-excerpt">Lorem ipsum dolor sit amet, consectetur adipiscing elit. Curabitur arcu diam, ornare vitae blandit sed, mollis pulvinar tortor...</p>
    </div>
    <div class="news-link">Read More <svg width="6" height="9" viewBox="0 0 6 9"><path d="M1,1 L4.5,4.5 L1,8" fill="none" stroke="#222" stroke-width="1.6"/></svg></div>
  </article>
</body>
</html>
```